Larkmoor Health- Core Values Graphic for Visual Appeal

I would like a poster that could take these written core values from our organization and create a graphic that we could use for our staff and employees. I would also like to incorporate our branding into this project. Thank you!

Target Market(s)

To helps patients and employees understand the core values of our organization

Industry/Entity Type

Healthcare

Requirements
Must have
• Match our branding
Nice to have
• Please use your creativity!
Should not have
• Overly complex/ busy

```html
<!DOCTYPE html>
<html lang="en">
<head>
<meta charset="utf-8">
<title>Larkmoor Health – Core Values</title>
<link href="https://fonts.googleapis.com/css2?family=Saira+Condensed:wght@700&family=Source+Sans+3:wght@400;600&display=swap" rel="stylesheet">
<style>
  :root {
    --paper: #f1f1f0;
    --ink: #1f1f20;
    --blue: #1f9ad6;
    --white: #ffffff;
    --texture: #d9d9d9;
  }
  * { margin: 0; padding: 0; box-sizing: border-box; }
  html, body { width: 998px; height: 1200px; overflow: hidden; }
  body {
    background: var(--paper);
    font-family: "Source Sans 3", "Myriad Pro", sans-serif;
    color: var(--ink);
  }
  .poster { position: relative; width: 998px; height: 1200px; }
  .shapes { position: absolute; inset: 0; }

  .poster-title {
    position: absolute;
    left: 470px; top: 52px;
    font-family: "Saira Condensed", "Oswald", sans-serif;
    font-weight: 700;
    font-size: 96px;
    line-height: 1;
    letter-spacing: -1px;
    color: var(--ink);
  }

  .value-name {
    position: absolute;
    font-family: "Saira Condensed", "Oswald", sans-serif;
    font-weight: 700;
    font-size: 60px;
    line-height: 1;
    letter-spacing: -0.5px;
    white-space: nowrap;
    transform: translate(-50%, -50%) rotate(var(--tilt));
  }
  .value-name--ink { color: var(--ink); }
  .value-name--blue { color: var(--blue); }

  .value-copy {
    position: absolute;
    width: 292px;
    font-size: 14.6px;
    line-height: 17.4px;
    text-align: center;
    color: var(--white);
  }

  .brand {
    position: absolute;
    left: 66px; top: 1092px;
    display: flex; align-items: center; gap: 10px;
    font-family: "Source Sans 3", sans-serif;
    font-weight: 600;
    font-size: 24px;
    color: var(--ink);
  }
  .brand-dot {
    width: 16px; height: 16px; border-radius: 50%;
    background: var(--blue);
  }
</style>
</head>
<body>
<main class="poster">
  <svg class="shapes" width="998" height="1200" viewBox="0 0 998 1200" aria-hidden="false">
    <defs>
      <radialGradient id="texture-fade" cx="50%" cy="50%" r="50%">
        <stop offset="0%" stop-color="var(--texture)" stop-opacity="0.7"/>
        <stop offset="100%" stop-color="var(--texture)" stop-opacity="0"/>
      </radialGradient>
      <path id="bulb" d="M -52,0 L 52,0 C 58,-70 95,-110 126,-139 A 165 165 0 1 0 -126,-139 C -95,-110 -58,-70 -52,0 Z"/>
    </defs>

    <ellipse class="texture" role="img" aria-label="Soft halftone dot texture" cx="190" cy="40" rx="120" ry="60" fill="url(#texture-fade)"/>
    <ellipse class="texture" role="img" aria-label="Soft halftone dot texture" cx="900" cy="1160" rx="140" ry="80" fill="url(#texture-fade)"/>

    <!-- bulbs: translate to neck bottom centre -->
    <use href="#bulb" class="bulb bulb--family" transform="translate(302 525)" fill="var(--blue)"/>
    <use href="#bulb" class="bulb bulb--integrity" transform="translate(674 661)" fill="var(--ink)"/>
    <use href="#bulb" class="bulb bulb--service" transform="translate(321 1021)" fill="var(--ink)"/>
    <use href="#bulb" class="bulb bulb--excellence" transform="translate(712 1119)" fill="var(--blue)"/>

    <!-- value icons -->
    <circle role="img" aria-label="Family icon" cx="302" cy="474" r="28" fill="var(--white)"/>
    <circle role="img" aria-label="Trust and handshake icon" cx="674" cy="596" r="28" fill="var(--blue)"/>
    <circle role="img" aria-label="Caring hands icon" cx="321" cy="967" r="28" fill="var(--blue)"/>
    <circle role="img" aria-label="Award ribbon icon" cx="712" cy="1052" r="28" fill="var(--white)"/>

    <!-- dotted rules -->
    <g class="rules" stroke-width="3" stroke-dasharray="2 5" stroke-linecap="round">
      <line x1="208" y1="538" x2="395" y2="538" stroke="var(--ink)"/>
      <line x1="579" y1="674" x2="766" y2="674" stroke="var(--blue)"/>
      <line x1="226" y1="1034" x2="413" y2="1034" stroke="var(--blue)"/>
      <line x1="619" y1="1133" x2="806" y2="1133" stroke="var(--ink)"/>
    </g>

    <!-- accent dots -->
    <circle cx="131" cy="476" r="20" fill="var(--ink)"/>
    <circle cx="877" cy="583" r="20" fill="var(--blue)"/>
    <circle cx="502" cy="645" r="30" fill="none" stroke="var(--blue)" stroke-width="18"/>
    <circle cx="530" cy="1092" r="21" fill="var(--ink)"/>
  </svg>

  <h1 class="poster-title">CORE VALUES</h1>

  <h2 class="value-name value-name--ink" style="left:150px; top:172px; --tilt:-42deg;">FAMILY</h2>
  <h2 class="value-name value-name--blue" style="left:814px; top:318px; --tilt:34deg;">INTEGRITY</h2>
  <h2 class="value-name value-name--blue" style="left:158px; top:690px; --tilt:-56deg;">SERVICE</h2>
  <h2 class="value-name value-name--ink" style="left:784px; top:752px; --tilt:25deg;">EXCELLENCE</h2>

  <p class="value-copy" style="left:156px; top:216px;">At the heart of our mission is the commitment to provide high-quality, affordable healthcare in a comforting and uplifting family-oriented environment. Just as our community is our extended family, every patient is a cherished member of our healthcare family. We treat each individual with the same care, compassion, and respect we would offer to our own loved ones.</p>

  <p class="value-copy" style="left:528px; top:351px;">In line with our goal, we aspire not only to alleviate pain but also to inspire patients to become active participants in their well-being. We believe in empowering our patients through education and compassion. Our pursuit of excellence is unwavering, driven by our dedication to continuously improve our services at every level, ensuring that our community receives nothing less than exceptional care.</p>

  <p class="value-copy" style="left:175px; top:712px;">In our healthcare team, ‘Integrity’ is non-negotiable. Our purpose is deeply rooted in ethics, integrity, and professional standards. We operate with the utmost integrity in every aspect of our work, adhering to the highest ethical principles. We understand that trust is the foundation of healthcare, and we are committed to maintaining the trust our community places in us.</p>

  <p class="value-copy" style="left:566px; top:813px;">Our vision is grounded in the belief that every person possesses the innate potential for true health. We aim to facilitate the body’s natural healing response by providing the highest level of service. Our hope for each patient extends beyond healing; we aspire to help you fulfill your life’s mission and purpose abundantly, supporting you in your journey to well-being.</p>

  <div class="brand">
    <span class="brand-dot"></span>
    <span class="brand-name">Larkmoor Health</span>
  </div>
</main>
</body>
</html>
```